Bramblecot Namecard

We have a regular but rotating group of Actors and Directors who meet weekly. I'd like to make a nametag (first and last names) for each of the participants which would fit on a regular business card. The first name would be over-sized to enable reading at a distance. The background & border should project fun and warmth. The Bramblecot is meant to be a place to play without judgement or negative vibes.

```html
<!DOCTYPE html>
<html lang="en">
<head>
<meta charset="UTF-8">
<title>Bramblecot Namecard</title>
<link rel="stylesheet" href="https://fonts.googleapis.com/css2?family=Gelasio:wght@400&family=Lobster+Two:ital,wght@1,700&family=Arimo:wght@700&display=swap">
<style>
  :root {
    --page: #f2f2f2;
    --card: #ffffff;
    --band-red: #a30d0d;
    --brand-red: #a30d0d;
    --panel-warm: #c85a32;
    --panel-dark: #323232;
    --type-light: #ffffff;
    --crowd-1: #7a4a3a;
    --crowd-2: #b03a2e;
    --crowd-3: #9c1c3c;
    --crowd-4: #a8522c;
  }
  * { box-sizing: border-box; margin: 0; padding: 0; }
  html, body {
    width: 1200px;
    height: 740px;
    overflow: hidden;
    background: var(--page);
  }
  .canvas {
    position: relative;
    width: 1200px;
    height: 740px;
    display: flex;
    align-items: center;
    justify-content: center;
    gap: 40px;
  }
  .namecard {
    position: relative;
    width: 540px;
    height: 330px;
    background: var(--card);
    border: 1px solid #222;
    box-shadow: 2px 3px 6px rgba(0,0,0,0.25);
    overflow: hidden;
  }
  .namecard--warm { --panel: var(--panel-warm); }
  .namecard--dark { --panel: var(--panel-dark); }
  .namecard__shapes {
    position: absolute;
    inset: 0;
    width: 100%;
    height: 100%;
  }
  .namecard__panel { fill: var(--panel); }
  .namecard__band { fill: var(--band-red); }
  .namecard__brand {
    position: absolute;
    left: 14px;
    top: 8px;
    font-family: "Arimo", Arial, sans-serif;
    font-weight: 700;
    font-size: 17px;
    color: var(--brand-red);
  }
  .namecard__first {
    position: absolute;
    left: 0;
    right: 0;
    top: 62px;
    text-align: center;
    font-family: "Gelasio", Georgia, serif;
    font-size: 104px;
    line-height: 1;
    color: var(--type-light);
  }
  .namecard__last {
    position: absolute;
    left: 0;
    right: 0;
    top: 172px;
    padding-left: 50px;
    text-align: center;
    font-family: "Lobster Two", cursive;
    font-style: italic;
    font-weight: 700;
    font-size: 44px;
    line-height: 1;
    color: var(--type-light);
  }
  .namecard__crowd {
    position: absolute;
    right: 14px;
    bottom: 8px;
    width: 82px;
    height: 44px;
    border-radius: 6px;
    background: linear-gradient(90deg, var(--crowd-1), var(--crowd-2), var(--crowd-3), var(--crowd-4));
  }
</style>
</head>
<body>
<main class="canvas">

  <article class="namecard namecard--warm">
    <svg class="namecard__shapes" viewBox="0 0 560 340" preserveAspectRatio="none" aria-hidden="true">
      <path class="namecard__panel" d="M0,52 C180,42 380,66 560,30 L560,276 C380,300 200,272 0,312 Z"/>
      <path class="namecard__band" d="M0,40 C180,30 380,54 560,16 L560,36 C380,72 180,50 0,62 Z"/>
      <path class="namecard__band" d="M0,304 C200,264 380,292 560,262 L560,284 C380,312 200,288 0,326 Z"/>
    </svg>
    <p class="namecard__brand">#Bramblecot</p>
    <h1 class="namecard__first">Name</h1>
    <p class="namecard__last">last name</p>
    <div class="namecard__crowd" role="img" aria-label="Small group of people figures in warm reds"></div>
  </article>

  <article class="namecard namecard--dark">
    <svg class="namecard__shapes" viewBox="0 0 560 340" preserveAspectRatio="none" aria-hidden="true">
      <path class="namecard__panel" d="M0,52 C180,42 380,66 560,30 L560,276 C380,300 200,272 0,312 Z"/>
      <path class="namecard__band" d="M0,40 C180,30 380,54 560,16 L560,36 C380,72 180,50 0,62 Z"/>
      <path class="namecard__band" d="M0,304 C200,264 380,292 560,262 L560,284 C380,312 200,288 0,326 Z"/>
    </svg>
    <p class="namecard__brand">#Bramblecot</p>
    <h1 class="namecard__first">Name</h1>
    <p class="namecard__last">last name</p>
    <div class="namecard__crowd" role="img" aria-label="Small group of people figures in warm reds"></div>
  </article>

</main>
</body>
</html>
```